Flyer-Design für Dekorations- und Farbkonzepte
hat alles bestens geklappt und tolles Design...kann Sie nur weiterempfehlen! PS. Lieben Dank für die Geduld! Beste Grüsse Rosalie Trachsler
Zielgruppe
Dekorationskonzepte, Farbkonzepte für Räume, Planung und Realisation Geschäfts - und Privatkunden, Zielgruppe Firmen, Seniorenheime , Privatkundschaft
Aufgabenstellung
Ich bin im Mai an einem Anlass in einem Seniorenheim und habe die Möglichkeit mich zu präsentieren , ich mache an diesem Anlass die Dekoration und möchte dabei Tag einen wertigen Flyer abgeben. An diesem Anlass sind auch der Gemeindepräsident und Angehörige der Bewohner etc . eingeladen. Der Flyer soll etwas gediegen daherkommen und über meine Arbeit informieren. Ich möchte vorallem Geschäftskunden ansprechen. Der Flyer sollte Emotionen wecken. Masse ca. A5 ..bin da sehr offen (nicht zu klein )

```html
<!DOCTYPE html>
<html lang="de">
<head>
<meta charset="utf-8">
<title>Raumklang – Flyer</title>
<link rel="stylesheet" href="https://fonts.googleapis.com/css2?family=Nothing+You+Could+Do&family=Crimson+Text:wght@400&family=Montserrat:wght@400&display=swap">
<style>
  :root {
    --paper: #ffffff;
    --edge: #c9d0db;
    --slate: #7d8ca2;
    --slate-light: #8e9cb1;
    --ink-light: #ffffff;
    --ink-soft: #eef0f4;
    --ink-muted: #b9c2d0;
  }
  * { margin: 0; padding: 0; box-sizing: border-box; }
  html, body { width: 846px; height: 1200px; overflow: hidden; background: var(--paper); }
  .flyer {
    position: relative;
    width: 846px;
    height: 1200px;
    background: var(--paper);
    border: 1px solid var(--edge);
  }
  .flyer__panel {
    position: absolute;
    left: 29px;
    top: 29px;
    width: 789px;
    height: 1142px;
    background: var(--slate);
    overflow: hidden;
  }
  .quote {
    position: absolute;
    left: 0;
    top: 180px;
    width: 789px;
    text-align: center;
    font-family: "Nothing You Could Do", cursive;
    font-size: 80px;
    line-height: 103px;
    color: var(--ink-light);
    letter-spacing: 2px;
  }
  .quote__author {
    position: absolute;
    right: 79px;
    top: 512px;
    font-family: "Crimson Text", serif;
    font-size: 20px;
    color: var(--ink-light);
  }
  .brand {
    position: absolute;
    left: 0;
    top: 925px;
    width: 789px;
    text-align: center;
  }
  .brand__mark {
    display: block;
    margin: 0 auto 22px;
  }
  .brand__name {
    font-family: "Crimson Text", serif;
    font-size: 38px;
    font-weight: 400;
    letter-spacing: 5px;
    color: var(--ink-soft);
    line-height: 1;
  }
  .brand__service {
    margin-top: 8px;
    font-family: "Nothing You Could Do", cursive;
    font-size: 18px;
    color: var(--ink-muted);
    letter-spacing: 1px;
  }
  .brand__audience {
    margin-top: 6px;
    font-family: "Montserrat", sans-serif;
    font-size: 10.5px;
    letter-spacing: 2px;
    color: var(--ink-soft);
  }
</style>
</head>
<body>
  <main class="flyer">
    <section class="flyer__panel">
      <blockquote class="quote">
        <p>„Der Stil erhält<br>die Schönheit<br>vom Gedanken.“</p>
      </blockquote>
      <p class="quote__author">Albrecht Sommerfeld</p>

      <footer class="brand">
        <svg class="brand__mark" width="40" height="40" viewBox="0 0 40 40" aria-hidden="true">
          <circle cx="20" cy="20" r="18" fill="var(--ink-muted)"/>
        </svg>
        <p class="brand__name">RAUMKLANG</p>
        <p class="brand__service">Einrichtungsberatung</p>
        <p class="brand__audience">FÜR GESCHÄFTS- UND PRIVATKUNDEN</p>
      </footer>
    </section>
  </main>
</body>
</html>
```